A bar in Newtown, NSW needs a website

We need a website design for a small speakeasy-style bar in Newtown, NSW Australia. The website needs to be simple to navigate, minimalistic, and feature light colours.

The functionality has to be fairly simple:

Main page (navigates to things below)
Food menu
Beverage menu
Bookings

Social media links and misc info at the bottom of every page.

The menus pages need to have space for text inserted as a jpeg file.

Name and logo are attached.

Coding

Coded - Design and coding required

Number of Pages Required

4 page

```html
<!DOCTYPE html>
<html lang="en">
<head>
<meta charset="utf-8">
<title>The Copper Lantern – Bar &amp; Kitchen</title>
<link rel="stylesheet" href="https://fonts.googleapis.com/css2?family=Cinzel:wght@400;600;700&family=Lato:wght@400;700;900&display=swap">
<style>
:root{
  --topbar:#1b1815;
  --wood-light:#e2bc84;
  --wood-mid:#d4a76b;
  --wood-dark:#c4935a;
  --ink:#1d1a17;
  --ink-soft:#3a3530;
  --section-bg:#f5f4f2;
  --line:#9a948c;
  --btn:#1c1c1c;
  --white:#ffffff;
  --field-border:#cfcfcf;
  --gallery-a:#1a2236;
  --gallery-b:#3a1d24;
  --frame:#d9d0c4;
}
*{box-sizing:border-box;margin:0;padding:0}
html,body{width:1200px;height:2390px;overflow:hidden}
body{position:relative;background:var(--section-bg);font-family:'Lato',sans-serif;color:var(--ink)}
.abs{position:absolute}

.topbar{left:0;top:0;width:1200px;height:64px;background:var(--topbar);color:#ddd;font-size:13px}
.topbar .hours{position:absolute;left:83px;top:0;height:64px;display:flex;align-items:center;gap:10px}
.topbar .social{position:absolute;right:83px;top:18px;display:flex;gap:14px}
.topbar .social span{width:28px;height:28px;border-radius:50%;background:#4a4541;display:block}

.header{left:0;top:64px;width:1200px;height:116px;background:linear-gradient(90deg,var(--wood-mid),var(--wood-light) 45%,var(--wood-mid) 80%,var(--wood-dark))}
.brand{position:absolute;left:83px;top:16px;display:flex;align-items:center;gap:10px}
.brand .mark{width:14px;height:14px;background:var(--ink)}
.brand .name{font-family:'Cinzel',serif;font-weight:700;font-size:26px;line-height:1;color:var(--ink);width:150px}
.contact-info{position:absolute;top:20px;display:flex;gap:10px;align-items:flex-start;font-size:12px;font-weight:700;line-height:17px;color:var(--ink)}
.nav{position:absolute;top:64px;left:373px;width:752px;display:flex;justify-content:space-between;height:52px;align-items:center}
.nav a{font-family:'Cinzel',serif;font-size:17px;letter-spacing:1px;text-transform:uppercase;color:var(--ink);text-decoration:none;padding:0 10px;height:52px;display:flex;align-items:center}
.nav a.active{background:var(--topbar);color:var(--white)}

.hero{left:0;top:180px;width:1200px;height:533px;background:radial-gradient(ellipse at 50% 35%,#6a4a32 0%,#3b2a1e 45%,#1c140e 100%)}
.hero-caption{position:absolute;left:0;right:0;bottom:0;height:92px;background:linear-gradient(rgba(0,0,0,0),rgba(0,0,0,.55));color:var(--white);font-weight:700;font-size:27px;text-align:center;padding-top:38px}
.hero-arrow{position:absolute;top:247px;width:40px;height:38px;background:rgba(60,60,60,.85);border:1px solid #999;display:flex;align-items:center;justify-content:center}

.section-title{left:0;width:1200px;text-align:center;font-family:'Cinzel',serif;font-weight:600;font-size:30px;letter-spacing:1px;text-transform:uppercase}
.rule{height:2px;width:58px;background:var(--line)}

.col-img{top:846px;width:333px;height:209px}
.col-title{top:1072px;font-family:'Cinzel',serif;font-weight:700;font-size:20px;letter-spacing:.5px;text-transform:uppercase}
.menu-item{width:333px;font-size:16px}
.menu-item .row{display:flex;align-items:baseline;gap:6px;font-weight:700}
.menu-item .row .dots{flex:1;border-bottom:1px dotted #999;transform:translateY(-3px)}
.menu-item .desc{font-size:12.5px;color:var(--ink-soft);margin-top:8px}
.btn{display:flex;align-items:center;justify-content:center;width:128px;height:37px;background:var(--btn);color:var(--white);font-size:14px;font-weight:700;text-transform:uppercase}
.field{left:786px;width:335px;height:38px;background:var(--white);border:1px solid var(--field-border);font-size:12.5px;color:var(--ink-soft);padding-left:13px;display:flex;align-items:center}
.field .addon{position:absolute;right:0;top:0;width:32px;height:36px;background:#d8d8d8;display:flex;align-items:center;justify-content:center}

.gallery{left:0;top:1435px;width:1200px;height:717px;background:radial-gradient(ellipse at 30% 20%,#5a2a2a 0%,var(--gallery-b) 30%,var(--gallery-a) 75%)}
.tile{border:2px solid var(--frame)}
.tile-caption{position:absolute;left:0;right:0;top:60px;color:var(--white);font-weight:700;font-size:20px;text-align:center;line-height:24px}

.footer{left:0;top:2152px;width:1200px;height:238px;background:linear-gradient(90deg,var(--wood-mid),var(--wood-light) 50%,var(--wood-mid));color:var(--white)}
.footer h4{position:absolute;top:30px;font-size:15px;font-weight:700;color:var(--ink)}
.footer .underline{position:absolute;top:53px;width:36px;height:1px;background:var(--ink)}
.quick-links{position:absolute;left:83px;top:66px;list-style:none;font-size:10.5px;font-weight:700}
.quick-links li{height:28px}
.quick-links li::before{content:"›";margin-right:10px}
.hours-block{position:absolute;left:260px;top:66px;font-size:10.5px;font-weight:700;line-height:15px}
.hours-block .label{font-size:13px;margin-top:10px;margin-bottom:2px}
.hours-block .phone{font-size:13.5px;margin-top:10px}
.map{position:absolute;left:488px;top:67px;width:188px;height:131px;background:linear-gradient(135deg,#d9e3c8,#c8d8e6 60%,#e6dcc4);border:2px solid var(--white)}
.follow{position:absolute;left:744px;top:67px;list-style:none;font-size:9.5px;font-weight:700}
.follow li{display:flex;align-items:center;gap:10px;height:35px}
.follow li span{width:26px;height:26px;border-radius:50%;background:var(--white);display:block}
.footer-brand{position:absolute;left:945px;top:64px;display:flex;align-items:center;gap:8px}
.footer-brand .name{font-family:'Cinzel',serif;font-weight:700;font-size:24px;line-height:1;color:var(--ink);width:140px}
.footer-brand .mark{width:12px;height:12px;background:var(--ink)}
.copyright{position:absolute;left:895px;width:240px;top:172px;text-align:center;font-size:10.5px;font-weight:700;line-height:15px}
</style>
</head>
<body>

<div class="abs topbar">
  <div class="hours">
    <svg width="20" height="20" viewBox="0 0 20 20"><circle cx="10" cy="10" r="8.5" fill="none" stroke="#ddd" stroke-width="1.5"/><path d="M10 5v5l3 2" fill="none" stroke="#ddd" stroke-width="1.5"/></svg>
    Monday - Sunday 10:00 am - 11:00 pm
  </div>
  <div class="social" aria-label="Social links"><span></span><span></span><span></span><span></span></div>
</div>

<header class="abs header">
  <div class="brand"><span class="mark"></span><span class="name">The Copper Lantern</span></div>
  <div class="contact-info" style="left:701px">
    <svg width="20" height="26" viewBox="0 0 20 26"><path d="M10 2a7 7 0 0 0-7 7c0 5 7 14 7 14s7-9 7-14a7 7 0 0 0-7-7z" fill="none" stroke="#1d1a17" stroke-width="2"/><circle cx="10" cy="9" r="2.5" fill="none" stroke="#1d1a17" stroke-width="2"/></svg>
    <div>48 Kingsway Lane<br>Eastbrook Quarter NSW 2042</div>
  </div>
  <div class="contact-info" style="left:948px">
    <svg width="26" height="26" viewBox="0 0 26 26"><path d="M6 3l4 5-2 3c1.5 3 4 5.5 7 7l3-2 5 4-2 4C12 23 3 14 3 5z" fill="none" stroke="#1d1a17" stroke-width="2" stroke-linejoin="round"/></svg>
    <div>02 9555 0142<br>hello@copperlantern.com</div>
  </div>
  <nav class="nav">
    <a class="active" href="#">Home</a>
    <a href="#">Food Menu</a>
    <a href="#">Beverage Menu</a>
    <a href="#">Bookings</a>
    <a href="#">Contact Us</a>
  </nav>
</header>

<section class="abs hero" role="img" aria-label="Photo of the dim bar interior with brick walls, bar counter, stools and wooden benches">
  <div class="hero-arrow" style="left:6px"><svg width="12" height="14"><path d="M9 1L2 7l7 6z" fill="#fff"/></svg></div>
  <div class="hero-arrow" style="left:1154px"><svg width="12" height="14"><path d="M3 1l7 6-7 6z" fill="#fff"/></svg></div>
  <div class="hero-caption">Lorem ipsum dolor sit amet, consectetuer adipiscing</div>
</section>

<h1 class="abs section-title" style="top:760px">Welcome to The Copper Lantern</h1>
<div class="abs rule" style="left:571px;top:815px"></div>

<div class="abs col-img" style="left:83px;background:linear-gradient(135deg,#8fa06a,#d8c8a0 50%,#7a3a22)" role="img" aria-label="Photo of a noodle dish with tempura"></div>
<h2 class="abs col-title" style="left:83px">Food Menu</h2>
<div class="abs rule" style="left:83px;top:1107px"></div>
<div class="abs menu-item" style="left:83px;top:1134px"><div class="row">CORVINA TIRADITO<span class="dots"></span>$12</div><div class="desc">Avocado / Apple / Dired tuna / radish</div></div>
<div class="abs menu-item" style="left:83px;top:1207px"><div class="row">LOBSTER ROLL<span class="dots"></span>$16</div><div class="desc">With house made old bay patato</div></div>
<div class="abs menu-item" style="left:83px;top:1273px"><div class="row">BEEF TATAKI<span class="dots"></span>$12</div><div class="desc">Unagi / Eggplant caviar / Picked carrots</div></div>
<div class="abs btn" style="left:83px;top:1347px">Read More</div>

<div class="abs col-img" style="left:434px;background:linear-gradient(90deg,#6a4a30,#b07a3a 45%,#e8c070 70%,#8a6a4a)" role="img" aria-label="Photo of fried chicken with fries and a mug of beer"></div>
<h2 class="abs col-title" style="left:439px">Beverage Menu</h2>
<div class="abs rule" style="left:439px;top:1107px"></div>
<div class="abs menu-item" style="left:439px;top:1134px"><div class="row">CAESAR SALAD<span class="dots"></span>$08</div><div class="desc">Romaine / Ancovies / Croutons</div></div>
<div class="abs menu-item" style="left:439px;top:1207px"><div class="row">MIZUNA SALAD<span class="dots"></span>$12</div><div class="desc">Truffe vinaigrette / Murcott tangerine</div></div>
<div class="abs menu-item" style="left:439px;top:1273px"><div class="row">CORN SOUP<span class="dots"></span>$15</div><div class="desc">Dungeness crab gratin /Chipotle gelée</div></div>
<div class="abs btn" style="left:437px;top:1347px">Read More</div>

<div class="abs col-img" style="left:786px;width:335px;background:linear-gradient(180deg,#c89a50,#6a4428 55%,#d8d0c0)" role="img" aria-label="Photo of a dining room with set tables and warm lights"></div>
<h2 class="abs col-title" style="left:786px">Bookings</h2>
<div class="abs rule" style="left:786px;top:1107px"></div>
<div class="abs field" style="top:1135px">Name</div>
<div class="abs field" style="top:1181px">E-mail</div>
<div class="abs field" style="top:1229px">No. Of Persons<span class="addon"><svg width="12" height="8"><path d="M0 0h12L6 7z" fill="#fff"/></svg></span></div>
<div class="abs field" style="top:1277px">Date<span class="addon"><svg width="14" height="14"><rect x="1" y="2" width="12" height="11" fill="none" stroke="#fff" stroke-width="1.5"/><path d="M1 6h12M4 1v3M10 1v3" stroke="#fff" stroke-width="1.5"/></svg></span></div>
<div class="abs btn" style="left:786px;top:1347px">Book Now</div>

<section class="abs gallery">
  <h2 class="abs section-title" style="top:57px;color:var(--white)">Photo Gallery</h2>
  <div class="abs rule" style="left:571px;top:111px;background:#ccc"></div>
  <div class="abs tile" style="left:83px;top:154px;width:199px;height:493px;background:linear-gradient(180deg,#5a3a22,#2a1a12 60%,#4a2a1a)" role="img" aria-label="Photo of a wine bottle and glass of red wine"></div>
  <div class="abs tile" style="left:290px;top:149px;width:324px;height:324px;background:linear-gradient(135deg,#c04a2a,#a0602a 50%,#6a8a3a)" role="img" aria-label="Photo of roast meat with vegetables and wine"></div>
  <div class="abs tile" style="left:290px;top:479px;width:324px;height:171px;background:linear-gradient(135deg,#b07a3a,#7a4a22)" role="img" aria-label="Photo of fried snacks">
    <div class="tile-caption">Lorem ipsum dolor sit amet,<br>consectetuer adipiscing</div>
  </div>
  <div class="abs tile" style="left:623px;top:153px;width:287px;height:256px;background:linear-gradient(180deg,#3a2a22,#4a6a8a 60%,#d89a3a)" role="img" aria-label="Photo of colourful cocktails on a bar"></div>
  <div class="abs tile" style="left:623px;top:416px;width:140px;height:232px;background:linear-gradient(180deg,#d09a4a,#7a3a1a 60%,#5a7a2a)" role="img" aria-label="Photo of a burger"></div>
  <div class="abs tile" style="left:772px;top:416px;width:138px;height:232px;background:linear-gradient(180deg,#8a5a3a,#2a1a1a 60%,#d8d0c8)" role="img" aria-label="Photo of two wine bottles"></div>
  <div class="abs tile" style="left:920px;top:151px;width:201px;height:497px;background:linear-gradient(180deg,#a04020,#d8a060 50%,#b03a22)" role="img" aria-label="Photo of grilled skewers"></div>
</section>

<footer class="abs footer">
  <h4 style="left:83px">Quick Links</h4><span class="underline" style="left:83px"></span>
  <ul class="quick-links"><li>Home</li><li>Food Menu</li><li>Beverage Menu</li><li>Bookings</li><li>Contact Us</li></ul>

  <h4 style="left:260px">Opening Hours</h4><span class="underline" style="left:260px"></span>
  <div class="hours-block">
    Monday - Sunday<br>10:00 am - 11:00 pm
    <div class="label">Address</div>
    48 Kingsway Lane,<br>Eastbrook NSW 2042
    <div class="phone">Ph. 02 9555 0142</div>
  </div>

  <h4 style="left:486px">Location Map</h4><span class="underline" style="left:486px"></span>
  <div class="map" role="img" aria-label="Street map showing the bar location"></div>

  <h4 style="left:744px">Follow Us</h4><span class="underline" style="left:744px"></span>
  <ul class="follow"><li><span></span>FRIENDS</li><li><span></span>UPDATES</li><li><span></span>NETWORK</li><li><span></span>CIRCLES</li></ul>

  <div class="footer-brand"><span class="mark"></span><span class="name">The Copper Lantern</span></div>
  <div class="copyright">Copyright © 2016 The Copper Lantern.<br>All Right Reserved.</div>
</footer>

</body>
</html>
```